QWR Consulting Web Design… We need a Facelift!

We currently have a website but it is very outdated. We like our content, but could use some help on giving it a refreshed facelift.

www.QWR-Consulting.example is our site

We only consult with large companies in the US that have sales over $250,000 a year, so looking to be high end yet approachable in our look.

Target Market(s)

Large corporations

Industry/Entity Type

Consulting

Coding

Coded - Design and coding required

Number of Pages Required

5+ page

Font styles to use
Serif
Sans Serif

Requirements
Must have
• We love our logo, keep that the same.
• The site colors can deviate from the logo, as long as it is complimentary
Nice to have
• We like our videos and graphics. If you can make them better, then great! But you can also feel free to reuse them.
• There is a video on the opening screen and one on the video page.
• We would like the video on the video page to be incorporated on the first page.
• If you think we need other/more page, we are all ears!
Should not have
• Want to set us apart from our competition in look, feel, professionalism and step away from the old fashioned conservatives of their websites. We want to be professional, yet bolder and fresher.
• Our Competition is LedgerBrook.example and TheHallowayPartners.example, but not looking to copy of emulate them, but gives an idea of the world QWR is in.

```html
<!DOCTYPE html>
<html lang="en">
<head>
<meta charset="utf-8">
<title>QWR Consulting</title>
<link rel="stylesheet" href="https://fonts.googleapis.com/css2?family=Open+Sans:wght@400;600;700;800&family=Raleway:wght@300;400&family=Arimo:wght@400;700&display=swap">
<style>
:root{
  --red:#a8170b;
  --red-deep:#8f1207;
  --red-bright:#c2281b;
  --red-mid:#b01d10;
  --ink:#222;
  --text:#555;
  --grey-bg:#e8e8e8;
  --dark:#2a2a2a;
  --darker:#161616;
  --blue:#2f9fdc;
  --white:#fff;
}
*{box-sizing:border-box;margin:0;padding:0}
html,body{width:1200px;height:3141px;overflow:hidden}
body{font-family:"Arimo",Arial,sans-serif;color:var(--ink);background:var(--white);position:relative}
.abs{position:absolute}

/* top bar */
.topbar{position:absolute;left:0;top:0;width:1200px;height:34px;background:#1d1d1d;color:#ddd;font-size:11px;letter-spacing:.5px}
.topbar .welcome{position:absolute;left:68px;top:11px}
.topbar .login{position:absolute;left:1013px;top:0;width:118px;height:34px;background:var(--red);color:#fff;font-weight:700;font-size:13px;display:flex;align-items:center;justify-content:center;gap:6px}

/* header */
.header{position:absolute;left:0;top:34px;width:1200px;height:134px;background:#fff}
.brand{position:absolute;left:72px;top:32px;display:flex;align-items:center;gap:12px}
.brand .dot{width:48px;height:48px;border-radius:50%;background:var(--red)}
.brand .name{font-family:"Open Sans",sans-serif;font-weight:700;font-size:26px;color:#3a3a3a;line-height:1}
.contact-item{position:absolute;top:52px;display:flex;gap:10px;align-items:flex-start}
.contact-item .ico{width:36px;height:36px;background:var(--red);border-radius:3px;display:flex;align-items:center;justify-content:center}
.contact-item .lbl{font-size:11px;color:#666;margin-top:2px}
.contact-item .val{font-size:14px;font-weight:700;color:#222;margin-top:3px}

/* nav */
.nav{position:absolute;left:0;top:168px;width:1200px;height:42px;background:var(--red);display:flex;align-items:center}
.nav a{color:#fff;text-decoration:none;font-size:14px;height:42px;display:flex;align-items:center;padding:0 20px}
.nav a:first-child{margin-left:48px;background:var(--red-deep)}
.nav .search{position:absolute;left:928px;top:5px;width:202px;height:32px;background:#fff;display:flex;align-items:center;justify-content:space-between;padding:0 10px;color:#aaa;font-size:12px}

/* hero */
.hero{position:absolute;left:0;top:210px;width:1200px;height:700px;background:linear-gradient(100deg,#dfe9f4 0%,#b9cde0 45%,#5b6f86 75%,#2d3746 100%)}
.hero h1{position:absolute;left:75px;top:152px;font-family:"Open Sans",sans-serif;font-weight:800;font-size:46px;letter-spacing:2px;color:#1f2328}
.hero p{position:absolute;left:75px;top:222px;width:425px;font-size:16px;line-height:21px;color:#333}
.hero .join{position:absolute;left:71px;top:351px;width:161px;height:46px;background:var(--red);color:#fff;font-weight:700;font-size:14px;display:flex;align-items:center;justify-content:center}
.hero .prev{position:absolute;left:0;top:253px;width:42px;height:92px;background:rgba(90,100,115,.75);display:flex;align-items:center;justify-content:center}

/* features */
.features{position:absolute;left:61px;top:824px;width:1059px;display:flex}
.feature{position:relative;width:212px;height:260px;color:#fff;text-align:center;padding:70px 16px 0}
.feature:nth-child(1){background:var(--red-mid)}
.feature:nth-child(2){background:var(--red-bright)}
.feature:nth-child(3){background:var(--red-deep);margin-top:-25px;height:300px;padding-top:118px}
.feature:nth-child(4){background:var(--red-bright)}
.feature:nth-child(5){background:var(--red-mid)}
.feature .badge{position:absolute;left:50%;top:-35px;transform:translateX(-50%);width:74px;height:74px;border-radius:50%;background:var(--red);border:5px solid #fff;display:flex;align-items:center;justify-content:center}
.feature:nth-child(3) .badge{top:14px;width:86px;height:86px;background:#fff;border-color:var(--red-deep);box-shadow:0 0 0 3px #fff}
.feature h3{font-family:"Open Sans",sans-serif;font-weight:700;font-size:17px;letter-spacing:.6px;line-height:19px;margin-bottom:10px;min-height:38px;display:flex;align-items:center;justify-content:center}
.feature p{font-size:13px;line-height:16px;height:64px}
.feature .more{display:inline-block;margin-top:18px;background:#2b2b2b;color:#fff;font-size:12px;padding:9px 15px}
.feature:nth-child(3) .more{background:#fff;color:#222}

/* section titles */
.sec-title{position:absolute;left:0;width:1200px;text-align:center;font-family:"Raleway",sans-serif;font-weight:300;font-size:42px;letter-spacing:2px;color:#2a2a2a}
.sec-rule{position:absolute;left:570px;width:60px;height:3px;background:var(--red)}

.who-quote{position:absolute;left:0;top:1254px;width:1200px;text-align:center;font-size:15px;font-weight:700;color:#333}
.who-quote b{color:var(--red);font-size:20px}
.who-text{position:absolute;left:140px;top:1292px;width:920px;text-align:center;font-size:13px;line-height:17px;color:#666}

/* video band */
.video-band{position:absolute;left:0;top:1372px;width:1200px;height:380px;background:var(--red)}
.video-band h2{position:absolute;left:0;top:28px;width:1200px;text-align:center;font-family:"Open Sans",sans-serif;font-weight:700;font-size:25px;color:#fff;letter-spacing:.3px}
.video-band .hands{position:absolute;left:60px;top:82px;width:600px;height:298px;background:linear-gradient(180deg,#b32218,#d9a78d 70%,#c98a72)}
.tablet{position:absolute;left:136px;top:83px;width:513px;height:297px;background:#f4f4f4;border-radius:18px 18px 0 0;padding:28px 32px 0}
.tablet .screen{width:100%;height:269px;background:linear-gradient(135deg,#c9d3dc,#8a9aa9 60%,#5e6b78);position:relative}
.tablet .play{position:absolute;left:50%;top:105px;transform:translateX(-50%);width:48px;height:34px;background:#e52d27;border-radius:7px;display:flex;align-items:center;justify-content:center}
.tablet .bar{position:absolute;left:0;bottom:0;width:100%;height:22px;background:#111;display:flex;align-items:center;padding:0 10px;gap:10px}
.tablet .track{flex:1;height:4px;background:#555;position:relative}
.tablet .track i{position:absolute;left:0;top:0;width:40%;height:4px;background:#d52b1e}
.video-band .copy{position:absolute;left:727px;top:94px;width:400px;color:#fff;font-size:13.5px;line-height:18px}
.video-band .copy p{margin-bottom:16px}
.video-band .cta{position:absolute;left:729px;top:255px;width:184px;height:48px;background:var(--blue);color:#fff;font-size:15px;display:flex;align-items:center;justify-content:center;gap:10px}
.video-band .dots{position:absolute;left:1068px;top:358px;display:flex;gap:4px}
.video-band .dots i{width:8px;height:8px;background:#fff}
.video-band .dots i:first-child{background:var(--blue)}

/* why cards */
.why{position:absolute;left:46px;top:1937px;display:flex;gap:21px}
.why-card{position:relative;width:201px;height:356px;background:#f7f7f7;border:1px solid #e2e2e2;text-align:center;padding:6px}
.why-card .photo{width:100%;height:136px}
.why-card .circ{position:absolute;left:50%;top:100px;transform:translateX(-50%);width:84px;height:84px;border-radius:50%;background:var(--red);display:flex;align-items:center;justify-content:center}
.why-card h3{margin-top:62px;font-family:"Open Sans",sans-serif;font-weight:700;font-size:19px;color:#222}
.why-card p{margin:14px 10px 0;font-family:"Open Sans",sans-serif;font-size:13.5px;line-height:18px;color:#444}

/* testimonials */
.clients{position:absolute;left:0;top:2366px;width:758px;height:450px;background:var(--grey-bg)}
.clients h2{position:absolute;left:0;top:30px;width:758px;text-align:center;font-family:"Raleway",sans-serif;font-weight:300;font-size:46px;letter-spacing:1px;color:#222}
.clients .rule{position:absolute;left:349px;top:100px;width:60px;height:3px;background:var(--red)}
.clients .sub{position:absolute;left:0;top:112px;width:758px;text-align:center;font-weight:700;font-size:14px;color:#444}
.clients .avatar{position:absolute;left:329px;top:147px;width:100px;height:100px;border-radius:50%;background:linear-gradient(180deg,#c4241a,#a11a10)}
.clients blockquote{position:absolute;left:80px;top:278px;width:600px;text-align:center;font-size:13px;line-height:18px;color:#222}
.clients .who1{position:absolute;left:0;top:350px;width:758px;text-align:center;font-size:13px;font-weight:700}
.clients .who2{position:absolute;left:0;top:373px;width:758px;text-align:center;font-size:13px}
.clients .who2 span{color:var(--red)}
.clients .dots{position:absolute;left:370px;top:410px;display:flex;gap:4px}
.clients .dots i{width:7px;height:7px;background:#333}
.clients .dots i:first-child{background:var(--red)}

.feedback{position:absolute;left:758px;top:2366px;width:442px;height:450px;background:var(--red);color:#fff;padding:30px 24px 0 24px}
.feedback h2{font-family:"Open Sans",sans-serif;font-weight:700;font-size:28px;line-height:33px}
.feedback p{margin-top:14px;font-size:11.5px;line-height:15px;width:390px}
.feedback .field{margin-left:36px;width:270px;height:40px;background:#f0e5e5;color:#aaa;font-size:11px;padding:12px 10px;margin-top:8px}
.feedback .field:first-of-type{margin-top:20px}
.feedback .field.msg{height:74px}
.feedback .submit{margin-left:36px;margin-top:8px;width:110px;height:40px;background:var(--blue);color:#fff;font-weight:700;font-size:14px;display:flex;align-items:center;justify-content:center}

/* footer */
.footer{position:absolute;left:0;top:2816px;width:1200px;height:298px;background:var(--dark);color:#eee}
.fcol{position:absolute;top:40px}
.fcol h4{font-family:"Open Sans",sans-serif;font-weight:700;font-size:21px;color:var(--blue);margin-bottom:20px}
.fcol p{font-size:12px;line-height:16px}
.fcol ul{list-style:none}
.fcol li{font-size:12px;margin-bottom:13px;padding-left:16px;position:relative}
.fcol li::before{content:"";position:absolute;left:0;top:5px;width:4px;height:4px;background:var(--blue);border-radius:50%}
.fcol .in{width:200px;height:32px;background:#fff;color:#999;font-size:11px;padding:9px 8px;margin-bottom:6px}
.fcol .in.big{height:66px}
.fcol .send{width:84px;height:32px;background:var(--blue);color:#fff;font-weight:700;font-size:14px;display:flex;align-items:center;justify-content:center;margin-top:8px}
.fcol .line{display:flex;gap:12px;align-items:flex-start;font-size:12px;line-height:16px;margin-top:14px}
.copyright{position:absolute;left:0;top:3114px;width:1200px;height:27px;background:var(--darker);color:#ccc;font-size:11px;text-align:center;line-height:27px}
</style>
</head>
<body>

<div class="topbar">
  <span class="welcome">WELCOME VISITOR</span>
  <span class="login"><svg width="12" height="12" viewBox="0 0 12 12"><path d="M1 1h5v2H3v6h3v2H1z M6 3l4 3-4 3V7H4V5h2z" fill="#fff"/></svg>Login Here</span>
</div>

<header class="header">
  <div class="brand"><span class="dot"></span><span class="name">QWR Consulting</span></div>
  <div class="contact-item" style="left:452px">
    <span class="ico"><svg width="18" height="18" viewBox="0 0 18 18"><circle cx="9" cy="9" r="7" fill="none" stroke="#fff" stroke-width="2"/><path d="M5 9h8M9 2c-3 4-3 10 0 14M9 2c3 4 3 10 0 14" stroke="#fff" stroke-width="1.4" fill="none"/></svg></span>
    <div><div class="lbl">Visit Here</div><div class="val">418 Harlow Crest Avenue</div></div>
  </div>
  <div class="contact-item" style="left:733px">
    <span class="ico"><svg width="18" height="18" viewBox="0 0 18 18"><path d="M4 2l3 0 1 4-2 1c1 2 3 4 5 5l1-2 4 1v3c0 1-1 2-2 2C8 16 2 10 2 4c0-1 1-2 2-2z" fill="#fff"/></svg></span>
    <div><div class="lbl">Call Us</div><div class="val">(555) 0142 887</div></div>
  </div>
  <div class="contact-item" style="left:894px">
    <span class="ico"><svg width="18" height="14" viewBox="0 0 18 14"><rect x="1" y="1" width="16" height="12" fill="none" stroke="#fff" stroke-width="2"/><path d="M1 1l8 7 8-7" stroke="#fff" stroke-width="2" fill="none"/></svg></span>
    <div><div class="lbl">Email Us</div><div class="val">info@QWR-Consulting.example</div></div>
  </div>
</header>

<nav class="nav">
  <a>Why QWR</a><a>Our Process</a><a>Contact Us</a><a>About Us</a><a>Negotiating Bank Fees Tips</a><a>Client List</a>
  <span class="search">Search Site<svg width="16" height="16" viewBox="0 0 16 16"><circle cx="6.5" cy="6.5" r="5" fill="none" stroke="#333" stroke-width="2"/><path d="M10 10l5 5" stroke="#333" stroke-width="2"/></svg></span>
</nav>

<section class="hero">
  <div class="abs" style="left:0;top:0;width:1200px;height:700px" role="img" aria-label="Photo of two businessmen reviewing treasury figures at a desk"></div>
  <h1>LEDGER SCOUT</h1>
  <p>way to manage your treasury management feesway to manage your treasury management feesway to manage your treasury management feesway to manage your treasury management fees</p>
  <span class="join">JOIN US</span>
  <span class="prev"><svg width="14" height="26" viewBox="0 0 14 26"><path d="M12 2L2 13l10 11" stroke="#fff" stroke-width="3" fill="none"/></svg></span>
</section>

<div class="features">
  <div class="feature">
    <span class="badge"><svg width="30" height="28" viewBox="0 0 30 28"><path d="M15 1L2 8h26z M4 10h22v2H4z M6 13h3v9H6z M13 13h3v9h-3z M20 13h3v9h-3z M2 23h26v3H2z" fill="#fff"/></svg></span>
    <h3>Know The Market</h3>
    <p>Focusing on your business not on banking. Even in today's information age it is exceedingly difficult.</p>
    <span class="more">Read More</span>
  </div>
  <div class="feature">
    <span class="badge"><svg width="30" height="30" viewBox="0 0 30 30"><circle cx="13" cy="17" r="10" fill="none" stroke="#fff" stroke-width="2.5"/><text x="13" y="22" font-size="13" font-weight="700" fill="#fff" text-anchor="middle" font-family="Arial">$</text><path d="M20 3h8v8M28 3l-8 8" stroke="#fff" stroke-width="2.5" fill="none"/></svg></span>
    <h3>Understand Profitability</h3>
    <p>Pricing is determined by profitability more than any other factor. QWR Consulting provides</p>
    <span class="more">Read More</span>
  </div>
  <div class="feature">
    <span class="badge"><svg width="38" height="28" viewBox="0 0 38 28"><circle cx="9" cy="8" r="5" fill="var(--red)"/><circle cx="19" cy="6" r="5.5" fill="var(--red)"/><circle cx="29" cy="8" r="5" fill="var(--red)"/><path d="M1 24c0-7 4-10 8-10s8 3 8 10z M11 24c0-8 4-11 8-11s8 3 8 11z M21 24c0-7 4-10 8-10s8 3 8 10z" fill="var(--red)"/></svg></span>
    <h3>Augment Your Team</h3>
    <p>Add to what your treasury team is already doing. Your team may already have completed</p>
    <span class="more">Read More</span>
  </div>
  <div class="feature">
    <span class="badge"><svg width="30" height="30" viewBox="0 0 30 30"><rect x="3" y="3" width="10" height="10" fill="#fff"/><rect x="17" y="3" width="10" height="10" fill="#fff"/><rect x="3" y="17" width="10" height="10" fill="#fff"/><rect x="17" y="17" width="10" height="10" fill="#fff"/></svg></span>
    <h3>What Banks What</h3>
    <p>Understand the many cards you have in your hand to play. Although bankers have an incentive</p>
    <span class="more">Read More</span>
  </div>
  <div class="feature">
    <span class="badge"><svg width="30" height="30" viewBox="0 0 30 30"><circle cx="12" cy="10" r="5" fill="#fff"/><path d="M2 27c0-8 4-11 10-11s10 3 10 11z" fill="#fff"/><circle cx="23" cy="8" r="5" fill="none" stroke="#fff" stroke-width="2"/><path d="M20 11l6-6" stroke="#fff" stroke-width="2"/></svg></span>
    <h3>Avoid Switching Providers</h3>
    <p>Appreciate the mutually beneficial relationship you have with your banker.</p>
    <span class="more">Read More</span>
  </div>
</div>

<h2 class="sec-title" style="top:1183px">WHO WE ARE</h2>
<div class="sec-rule" style="top:1238px"></div>
<p class="who-quote"><b>"</b> provide clarity and transparency to the treasury and cash management <b>"</b></p>
<p class="who-text">We are a consortium of ex-bankers, consultants, certified treasury professionals, and former practitioners that combined our resources with the objective of participating in a common activity for achieving a common goal: assisting clients in maximizing the return of their</p>

<section class="video-band">
  <h2>INTRODUCING A BRAND-NEW WAY TO MANAGE YOUR TREASURY MANAGEMENT FEES</h2>
  <div class="hands" role="img" aria-label="Photo of hands holding a tablet"></div>
  <div class="tablet">
    <div class="screen" role="img" aria-label="Video still of a business team gathered around a laptop">
      <span class="play"><svg width="14" height="16" viewBox="0 0 14 16"><path d="M1 1l12 7-12 7z" fill="#fff"/></svg></span>
      <div class="bar"><svg width="10" height="12" viewBox="0 0 10 12"><path d="M1 1l8 5-8 5z" fill="#fff"/></svg><span class="track"><i></i></span><svg width="12" height="10" viewBox="0 0 12 10"><path d="M1 3h3l4-3v10L4 7H1z" fill="#fff"/></svg><svg width="10" height="10" viewBox="0 0 10 10"><path d="M0 0h4v1H1v3H0zM10 0v4H9V1H6V0zM0 10V6h1v3h3v1zM10 10H6V9h3V6h1z" fill="#fff"/></svg></div>
    </div>
  </div>
  <div class="copy">
    <p>QWR Consulting works closely with your team assisting in auditing your bank fees and earnings credit rates. As former bankers, we bring our primary and regional bank experience to the table to supplement your team</p>
    <p>In providing insider knowledge for various bank pricing and net cost thresholds, so you can negotiate better pricing rates, and terms. Maximize return when you Manage Your Discount.</p>
  </div>
  <span class="cta"><svg width="22" height="22" viewBox="0 0 22 22"><circle cx="11" cy="11" r="10" fill="#fff"/><path d="M16 11H7M10 7l-4 4 4 4" stroke="var(--blue)" stroke-width="2.2" fill="none"/></svg>Check Our Video</span>
  <div class="dots"><i></i><i></i><i></i><i></i></div>
</section>

<h2 class="sec-title" style="top:1812px">WHY QWR?</h2>
<div class="sec-rule" style="top:1874px"></div>

<div class="why">
  <div class="why-card">
    <div class="photo" role="img" aria-label="Photo of a profits chart with a rising arrow" style="background:linear-gradient(135deg,#eee,#c9c9c9 60%,#b52a1f)"></div>
    <span class="circ"><svg width="40" height="34" viewBox="0 0 40 34"><path d="M3 2v29h35" stroke="#fff" stroke-width="3" fill="none"/><path d="M8 26l9-10 6 6 12-14" stroke="#fff" stroke-width="3.5" fill="none"/><path d="M29 7h7v7" stroke="#fff" stroke-width="3" fill="none"/></svg></span>
    <h3>Profitability</h3>
    <p>Clients enjoy gains they never thought possible by looking beyond market pricing and harnessing YRM™.</p>
  </div>
  <div class="why-card">
    <div class="photo" role="img" aria-label="Photo of business people silhouetted against a bright sky" style="background:linear-gradient(180deg,#e3e3e3,#9a9a9a 60%,#333)"></div>
    <span class="circ"><svg width="36" height="36" viewBox="0 0 36 36"><circle cx="18" cy="18" r="15" fill="none" stroke="#fff" stroke-width="2.5"/><circle cx="18" cy="13" r="5" fill="#fff"/><path d="M9 28c1-6 5-8 9-8s8 2 9 8z" fill="#fff"/></svg></span>
    <h3>Insiders</h3>
    <p>Our team has managed treasury personnel as well as client relation ships from within banks.</p>
  </div>
  <div class="why-card">
    <div class="photo" role="img" aria-label="Photo of many hands joined together" style="background:linear-gradient(135deg,#6b4b3a,#c99676 55%,#8a6a55)"></div>
    <span class="circ"><svg width="42" height="28" viewBox="0 0 42 28"><path d="M2 8l8-5 8 4 6-4 8 3 8 2v10l-6 2-10 7c-2 1-4 0-4-2l-3 1c-2 0-3-2-2-3l-3 0c-2-1-2-3-1-4L2 16z" fill="#fff"/></svg></span>
    <h3>Involved</h3>
    <p>Clients enjoy gains never possible before, with millions of dollars in actualized annual savings in their accounts.</p>
  </div>
  <div class="why-card">
    <div class="photo" role="img" aria-label="Photo of a woman looking through a magnifying glass" style="background:linear-gradient(135deg,#f2efec,#d6c6b8 55%,#7a5b46)"></div>
    <span class="circ"><svg width="34" height="34" viewBox="0 0 34 34"><path d="M17 2v30M2 17h30" stroke="#fff" stroke-width="3"/><path d="M12 7l5-5 5 5M12 27l5 5 5-5M7 12l-5 5 5 5M27 12l5 5-5 5" stroke="#fff" stroke-width="3" fill="none"/></svg></span>
    <h3>Thorough</h3>
    <p>A complete turn-key solution. We do the work, you make the decisions.</p>
  </div>
  <div class="why-card">
    <div class="photo" role="img" aria-label="Illustration of a figure in a blue data tunnel" style="background:radial-gradient(circle at 50% 50%,#e6eef8,#4f7ebf 55%,#1e3f78)"></div>
    <span class="circ"><svg width="36" height="32" viewBox="0 0 36 32"><rect x="3" y="3" width="8" height="26" fill="#fff"/><rect x="14" y="3" width="8" height="26" fill="#fff"/><rect x="24" y="5" width="8" height="25" fill="#fff" transform="rotate(-12 28 17)"/></svg></span>
    <h3>Data</h3>
    <p>Ledger Scout™ is our proprietary internet bot that systematically searches and indexes treasury pricing &amp; rates.</p>
  </div>
</div>

<section class="clients">
  <h2>WORDS FROM OUR CLIENTS</h2>
  <div class="rule"></div>
  <p class="sub">Our ability to love ourselves and the world is endless and powerful</p>
  <div class="avatar" role="img" aria-label="Portrait photo of the client"></div>
  <blockquote>In the 20 years I've been in treasury management, I really felt that I'd mastered our bank pricing. But when I started understanding bank's profitability so that I could laser focus on line items or rates for discussion, it became a game changer.</blockquote>
  <p class="who1">Treasurer of a National Retail Department Store</p>
  <p class="who2">Daniel K. Marlowe, Business Program Manager, <span>Northgate Civic Fund</span></p>
  <div class="dots"><i></i><i></i><i></i><i></i></div>
</section>

<section class="feedback">
  <h2>We welcome any and<br>all feedback</h2>
  <p>Lorem ipsum dolor sit amet, consectetur adipiscing elit. utate eu diam. Pellentesque molestie nisl in dolor gravida commo-do. Lorem ipsum dolor sit amet.</p>
  <div class="field">Name</div>
  <div class="field">Your Email</div>
  <div class="field msg">Your Message</div>
  <div class="submit">Submit</div>
</section>

<footer class="footer">
  <div class="fcol" style="left:88px;width:240px">
    <h4>About Us</h4>
    <p>We are a consortium of ex-bankers, consultants, certified treasury professionals, and former practitioners that combined our resources with the objective of participating in a common activity for achieving a common goal: assisting clients in maximizing the return of their</p>
  </div>
  <div class="fcol" style="left:387px">
    <h4>Our Services</h4>
    <ul><li>Our Process</li><li>Client List</li><li>About Us</li><li>Contact Us</li><li>Negotiating Bank Fees Tips</li><li>Search Advertising</li></ul>
  </div>
  <div class="fcol" style="left:628px">
    <h4>Ask Your Question</h4>
    <div class="in">Your Email</div>
    <div class="in big">Message</div>
    <div class="send">Send</div>
  </div>
  <div class="fcol" style="left:917px;width:250px">
    <h4>Contact Us</h4>
    <p>For all of your treasury and cash management fee, earnings credit rate, merchant card and purchase card needs.</p>
    <div class="line"><svg width="16" height="12" viewBox="0 0 16 12"><rect x="1" y="1" width="14" height="10" fill="none" stroke="var(--blue)" stroke-width="1.6"/><path d="M1 1l7 6 7-6" stroke="var(--blue)" stroke-width="1.6" fill="none"/></svg>hello@qwr-consulting.example</div>
    <div class="line"><svg width="16" height="16" viewBox="0 0 18 18"><path d="M4 2l3 0 1 4-2 1c1 2 3 4 5 5l1-2 4 1v3c0 1-1 2-2 2C8 16 2 10 2 4c0-1 1-2 2-2z" fill="var(--blue)"/></svg>P: (555) 0142 887</div>
    <div class="line"><svg width="14" height="18" viewBox="0 0 14 18"><path d="M7 1C3 1 1 4 1 7c0 4 6 10 6 10s6-6 6-10c0-3-2-6-6-6z" fill="var(--blue)"/><circle cx="7" cy="7" r="2.3" fill="var(--dark)"/></svg>418 Harlow Crest Avenue,<br>Fairmont, GA 30000</div>
  </div>
</footer>
<div class="copyright">© 2016 qwr-consulting.example All Right Reserved.</div>

</body>
</html>
```